Business card for a plastic surgeon

i need a business card for a plastic surgeon. I have two adresses. The card should communicate safety, simmetry, beauty and with soft colors.
What i want in the card:
- my logo: Letters "R"and "B" (picture uploaded)
- my name: Renato Bastiani
- my registration: CRM 507 219
- my adresses and phone numbers (2):
- Av Dr Teixeira Lopes, 2710, sala 305 - Vila Olímpia | São Paulo/ SP - Phone: 11 4172-5036
- Al. Itapeva, 47, 3 andar - Alphaville | Barueri/ SP - Phone: 11 6350-2481

- my social network: site, facebook and instagram

Target Market(s)

people (95% girls and women) that want cosmetic procedures and plastic surgery

Industry/Entity Type

Business

Contact Information for Business Card

The card should communicate safety, simmetry, beauty and with soft colors.
Beige, brown, gray, rosy are some options. Color is free

Font styles to use
Serif

Requirements
Must have
• - my logo: Letters "R"and "B" (picture uploaded)
• - my name: Renato Bastiani
• - my registration: CRM 507 219
• - my adresses and phone numbers (2):
• - Av Dr Teixeira Lopes, 2710, sala 305 - Vila Olímpia | São Paulo/ SP - Phone: 11 4172-5036
• - Al. Itapeva, 47, 3 andar - Alphaville | Barueri/ SP - Phone: 11 6350-2481
• - my social network: site, facebook and instagram
Should not have
• other images (only my logo)

```html
<!DOCTYPE html>
<html lang="pt-BR">
<head>
<meta charset="utf-8">
<title>Dr. Renato Bastiani – Cartão de visita</title>
<link rel="stylesheet" href="https://fonts.googleapis.com/css2?family=Cinzel:wght@400;500&family=Crimson+Text:wght@400;600&display=swap">
<style>
  :root {
    --bg: #5b5d60;
    --card-deep: #3fcdf6;
    --card-mid: #5edcf7;
    --card-light: #8ef0ef;
    --ink: #141414;
    --ink-soft: #6c7a82;
    --rule: #12b7ee;
    --mark-tint: rgba(255, 255, 255, 0.28);
  }
  * { box-sizing: border-box; margin: 0; padding: 0; }
  html, body { width: 1200px; height: 1016px; overflow: hidden; }
  body {
    background: var(--bg);
    font-family: "Crimson Text", Georgia, serif;
    color: var(--ink);
    position: relative;
  }
  .card {
    position: absolute;
    left: 220px;
    width: 760px;
    height: 430px;
    overflow: hidden;
  }
  .card--front {
    top: 40px;
    background: linear-gradient(115deg, var(--card-deep) 0%, var(--card-mid) 50%, #70e6f8 100%);
  }
  .card--back {
    top: 546px;
    background: linear-gradient(100deg, var(--card-deep) 0%, var(--card-mid) 45%, var(--card-light) 100%);
  }

  /* front */
  .monogram-halo {
    position: absolute;
    left: 50%;
    top: 40px;
    width: 210px;
    height: 210px;
    margin-left: -105px;
    border-radius: 50%;
    background: var(--mark-tint);
  }
  .monogram {
    position: absolute;
    left: 0; right: 0;
    top: 108px;
    text-align: center;
    font-family: "Cinzel", Georgia, serif;
    font-size: 64px;
    font-weight: 400;
    letter-spacing: 4px;
    color: var(--ink);
  }
  .front-name {
    position: absolute;
    left: 0; right: 0;
    top: 270px;
    text-align: center;
    font-family: "Cinzel", Georgia, serif;
    font-size: 40px;
    font-weight: 500;
    letter-spacing: 1px;
    color: var(--ink);
  }
  .front-title {
    position: absolute;
    left: 0; right: 0;
    top: 324px;
    text-align: center;
    font-family: "Cinzel", Georgia, serif;
    font-size: 21px;
    letter-spacing: 6px;
    color: var(--ink-soft);
  }

  /* back */
  .site {
    position: absolute;
    right: 40px;
    top: 22px;
    font-family: "Crimson Text", Georgia, serif;
    font-weight: 600;
    font-size: 27px;
    letter-spacing: 0.5px;
    color: var(--ink);
  }
  .site__domain { color: var(--ink-soft); font-weight: 400; }
  .identity {
    position: absolute;
    left: 32px;
    top: 228px;
  }
  .identity__name {
    font-family: "Cinzel", Georgia, serif;
    font-size: 32px;
    font-weight: 500;
    color: var(--ink);
  }
  .identity__role {
    margin-top: 6px;
    font-family: "Cinzel", Georgia, serif;
    font-size: 19px;
    letter-spacing: 1px;
    color: var(--ink-soft);
  }
  .identity__sep { margin: 0 6px; }
  .rule {
    position: absolute;
    left: 0; right: 0;
    top: 322px;
    height: 4px;
    background: var(--rule);
  }
  .office {
    position: absolute;
    top: 340px;
    font-size: 20px;
    line-height: 1.35;
  }
  .office--vila { left: 18px; }
  .office--alpha { left: 418px; top: 352px; }
  .office__area, .office__phone { color: var(--ink-soft); }
  .office__street { color: var(--ink); }
</style>
</head>
<body>
  <section class="card card--front" aria-label="Frente do cartão">
    <div class="monogram-halo"></div>
    <div class="monogram">RB</div>
    <h1 class="front-name">DR. RENATO BASTIANI</h1>
    <p class="front-title">CIRURGIÃO PLÁSTICO</p>
  </section>

  <section class="card card--back" aria-label="Verso do cartão">
    <p class="site">WWW.<span class="site__domain">DRRENATOBASTIANI</span>.COM.BR</p>
    <div class="identity">
      <h2 class="identity__name">DR. RENATO BASTIANI</h2>
      <p class="identity__role">CIRURGIÃO PLÁSTICO<span class="identity__sep">|</span>CRM 507219</p>
    </div>
    <div class="rule"></div>
    <address class="office office--vila" style="font-style:normal">
      <div class="office__area">Vila Olímpia</div>
      <div class="office__street">Av Dr Teixeira Lopes, 2710, sala 305</div>
      <div class="office__phone">11 4172 5036</div>
    </address>
    <address class="office office--alpha" style="font-style:normal">
      <div class="office__area">Alphaville</div>
      <div class="office__street">Al. Itapeva, 47, 3 andar</div>
      <div class="office__phone">11 6350 2481</div>
    </address>
  </section>
</body>
</html>
```